Crane of the future landing page

Brindle Systems manufactures smart products for overhead cranes, the kind you find in manufacturing plants and warehouses. Our products collect data on how the cranes are used, and by who and connect the equipment to the cloud (think IOT for cranes). We provide notifications when things (are about to) go wrong as well as information used to ensure compliance with safety laws. Our product website is brindlesystems.example.au and you can see an example of the data here: http://www.brindlesystems.example.au/?userID=exampledata (nb, that link will go to a HTML 5 version of the site on a mobile device).
Next year we want to launch these products into the US market, and the theme of that launch will be "The Crane of the Future" We need a single HTML5 landing page that uses parallax scrolling to make the following points:

The crane of the future will be smart.
The crane of the future will be connected.
The crane of the future will cost less and last longer.

The crane of the future is here.

Register to learn more

We will provide copy and base pictures (please use stock images in the first cut) for these points.
Nb, an overhead crane looks like this http://www.pictavault.example.com/photo/big-crane-5820394?st=k81f204

This is a mobile crane https://www.openlexis.example.org/wiki/Tarvell_Lifting#/media/File:Tarvell_Crane_in_Antarctica.jpg
This is a construction crane
http://railyardgame.fanpedia.example.com/wiki/Tower_Crane

Please only use images of overhead cranes

Target Market(s)

Industrial crane users, companies that supply and service overhead cranes

Industry/Entity Type

Digital

Coding

Coded - Design and coding required

Number of Pages Required

1 page

Font styles to use
Sans Serif

Requirements
Must have
• Image (maybe stylised) of a crane hoist ( this is the smart part of the crane) eg:
• http://www.keldorlift.example.com/products/wire-rope-hoists
• It must show that our systems collect data from cranes and send this data, along with alerts, to mobile phones
• Parallax scrolling
• Name/email capture form
Nice to have
• Keep it simple and as uncluttered as possible.
• Full screen image background,maybe subtly animated
• Most people seem to visualise a hook when the think of cranes, maybe something like
• http://www.pictavault.example.com/photo/worker-standing-by-a-big-crane-hook-29475310?st=k81f204
• Reference to the fact that the information is available on your PC/Phone???
• For your background info, this link will open a flash based PC app, or a HTML version on mobile devices: http://www.brindlesystems.example.au/?userID=exampledata
• Something that indicates that you get email/sms notification when things go wrong.
Should not have
• It's hard because there aren't a lot of generic stock photos, but try to avoid brand names.
• Don't include a copy of the menu from our website. This is a landing page, the only place the BrindleSystems logo and a link to the website should appear is under the section: "The crane of the future is here"

```html
<!DOCTYPE html>
<html lang="en">
<head>
<meta charset="utf-8">
<title>The Crane of the Future — Brindle Systems</title>
<link rel="stylesheet" href="https://fonts.googleapis.com/css2?family=Jost:wght@400;500;600&display=swap">
<style>
  :root {
    --ink-dark: #262626;
    --white: #ffffff;
    --hero-light: #8a8a8a;
    --hero-mid: #5a5a5a;
    --hero-deep: #2e2e2e;
    --crane-yellow: #e6b417;
    --crane-amber: #b98f1c;
    --crane-shadow: #6b5a2a;
    --soft-text: #d8d8d8;
  }
  * { margin: 0; padding: 0; box-sizing: border-box; }
  html, body { width: 849px; height: 1200px; overflow: hidden; }
  body {
    position: relative;
    background: var(--ink-dark);
    font-family: "Jost", "Futura", sans-serif;
    color: var(--white);
  }
  section, footer { position: absolute; left: 0; width: 849px; }

  /* Hero */
  .hero { top: 0; height: 500px; overflow: hidden; }
  .hero-photo {
    position: absolute; inset: 0;
    background: radial-gradient(ellipse 48% 55% at 52% 48%, var(--hero-light) 0%, var(--hero-mid) 55%, var(--hero-deep) 100%);
  }
  .hero-brand {
    position: absolute; top: 92px; left: 0; width: 100%;
    text-align: center; font-size: 18px; font-weight: 500; letter-spacing: 2px;
  }
  .hero-title {
    position: absolute; top: 152px; left: 0; width: 100%;
    text-align: center; font-size: 38px; font-weight: 600; letter-spacing: 1.5px; line-height: 57px;
  }
  .claim {
    position: absolute; font-size: 21px; font-weight: 500; letter-spacing: 0.8px; line-height: 1;
    padding-top: 9px;
  }
  .claim::before {
    content: ""; position: absolute; top: 0; height: 3px; width: 78px; background: var(--white);
  }
  .claim--left::before { left: 0; }
  .claim--right::before { right: 0; }
  .claim-last-longer { left: 100px; top: 172px; }
  .claim-smart { left: 678px; top: 172px; }
  .claim-cost-less { left: 211px; top: 323px; }
  .claim-connected { left: 502px; top: 323px; }
  .slide-dots { position: absolute; top: 369px; left: 395px; display: flex; gap: 6px; }
  .slide-dots span { width: 14px; height: 14px; border-radius: 50%; border: 2px solid var(--white); }
  .slide-dots .is-active { background: var(--white); }
  .scroll-down { position: absolute; top: 410px; left: 403px; }

  /* Features */
  .features { top: 500px; height: 258px; background: var(--white); }
  .feature-tile { position: absolute; top: 45px; width: 204px; height: 164px; }
  .tile-hoist { left: 94px; background: linear-gradient(180deg, var(--crane-yellow) 0%, #c79a12 45%, #8c7a55 70%, #a08a60 100%); }
  .tile-data { left: 322px; background: linear-gradient(90deg, #eef1ec 0%, #e4ece2 52%, #d9e9f4 60%, #f2f6f9 100%); }
  .tile-mobile { left: 552px; background: linear-gradient(135deg, #2c4f86 0%, #3f6aa8 45%, #c9a79a 70%, #2a4a7c 100%); }

  /* Crane is here */
  .arrival { top: 758px; height: 342px; overflow: hidden; }
  .arrival-photo {
    position: absolute; inset: 0;
    background: linear-gradient(90deg, var(--crane-yellow) 0%, var(--crane-amber) 25%, var(--crane-shadow) 50%, var(--crane-amber) 75%, var(--crane-yellow) 100%);
  }
  .arrival-copy {
    position: absolute; top: 45px; left: 0; width: 100%;
    text-align: center; font-size: 17px; font-weight: 500; line-height: 34px;
  }
  .arrival-title {
    position: absolute; top: 148px; left: 0; width: 100%;
    text-align: center; font-size: 32px; font-weight: 600; letter-spacing: 1.5px;
  }
  .arrival-badge {
    position: absolute; top: 194px; left: 355px; width: 140px; height: 41px;
    background: rgba(38,38,38,0.75);
    text-align: center; font-size: 32px; font-weight: 600; letter-spacing: 1.5px; line-height: 41px;
  }
  .scroll-up { position: absolute; top: 282px; left: 404px; }

  /* Footer */
  .site-footer { top: 1100px; height: 100px; background: var(--ink-dark); font-size: 14px; font-weight: 500; letter-spacing: 0.8px; line-height: 27px; }
  .footer-brand { position: absolute; left: 94px; top: 24px; }
  .footer-register { position: absolute; left: 0; width: 100%; top: 24px; text-align: center; }
  .footer-register .sub { font-weight: 400; color: var(--soft-text); }
  .footer-login { position: absolute; right: 94px; top: 24px; }
</style>
</head>
<body>
  <section class="hero">
    <div class="hero-photo" role="img" aria-label="Close-up of an overhead crane hoist with chain and hook, in soft greyscale"></div>
    <div class="hero-brand">BRINDLE SYSTEMS</div>
    <h1 class="hero-title">THE CRANE<br>OF THE FUTURE<br>WILL BE</h1>
    <div class="claim claim--left claim-last-longer">LAST LONGER</div>
    <div class="claim claim--right claim-smart">SMART</div>
    <div class="claim claim--left claim-cost-less">COST LESS</div>
    <div class="claim claim--right claim-connected">CONNECTED</div>
    <div class="slide-dots"><span class="is-active"></span><span></span><span></span></div>
    <svg class="scroll-down" width="44" height="34" viewBox="0 0 44 34" aria-hidden="true">
      <polyline points="3,3 22,18 41,3" fill="none" stroke="#fff" stroke-width="4"/>
      <polyline points="3,14 22,29 41,14" fill="none" stroke="#fff" stroke-width="4"/>
    </svg>
  </section>

  <section class="features">
    <div class="feature-tile tile-hoist" role="img" aria-label="Yellow overhead crane hoists hanging from a runway beam in a workshop"></div>
    <div class="feature-tile tile-data" role="img" aria-label="Screenshot of crane usage charts next to a phone alert email"></div>
    <div class="feature-tile tile-mobile" role="img" aria-label="Person in a blue suit checking a smartphone"></div>
  </section>

  <section class="arrival">
    <div class="arrival-photo" role="img" aria-label="Yellow overhead crane bridge spanning a factory bay, softly blurred"></div>
    <p class="arrival-copy">Lorem ipsum dolor sit amet, no duo doming audire. Ut<br>congue posidonium mel, nominavi incorrupte mei et</p>
    <h2 class="arrival-title">THE CRANE OF THE FUTURE</h2>
    <div class="arrival-badge">IS HERE</div>
    <svg class="scroll-up" width="42" height="30" viewBox="0 0 42 30" aria-hidden="true">
      <polyline points="3,16 21,3 39,16" fill="none" stroke="#fff" stroke-width="4"/>
      <polyline points="3,27 21,14 39,27" fill="none" stroke="#fff" stroke-width="4"/>
    </svg>
  </section>

  <footer class="site-footer">
    <div class="footer-brand">BRINDLE<br>SYSTEMS</div>
    <div class="footer-register">REGISTER<br><span class="sub">TO LEARN MORE</span></div>
    <div class="footer-login">LOG IN</div>
  </footer>
</body>
</html>
```